Rocket business card

Modern business card design, use of color is good with clean space too.

Things to include on card:

Quote: I add fuel to your optometry practice

- Eyewear Sales
- Admin Duties
- Revenue Collection
- Leadership
- Tech Adoption
- COGS Reduction
- Product Sourcing
-Medical Growth

Dalton Vesk, CEO
Lume Vantor
Text Me! 847-302-6194
dalton@lumevantor.net

```html
<!DOCTYPE html>
<html lang="en">
<head>
<meta charset="utf-8">
<title>Lume Vantor – Business Card</title>
<link rel="stylesheet" href="https://fonts.googleapis.com/css2?family=Montserrat:wght@400;500;700&display=swap">
<style>
  :root {
    --ink: #1f1f1f;
    --paper: #ffffff;
    --accent: #f5a31a;
    --accent-deep: #e8561f;
    --stage: #e6e6e6;
    --text-dark: #1a1a1a;
  }
  * { box-sizing: border-box; margin: 0; padding: 0; }
  html, body { width: 1200px; height: 900px; overflow: hidden; }
  body {
    background: var(--stage);
    font-family: "Montserrat", Arial, sans-serif;
    display: flex; flex-direction: column; align-items: center; justify-content: center; gap: 30px;
  }
  .card {
    position: relative; width: 720px; height: 400px; border-radius: 18px; overflow: hidden;
    box-shadow: 0 6px 18px rgba(0,0,0,.18);
  }
  .brand-dot { border-radius: 50%; background: var(--accent-deep); flex: none; }
  .brand-name { font-weight: 500; letter-spacing: 2px; text-transform: uppercase; white-space: nowrap; }

  /* Back side */
  .card--back { background: var(--ink); color: var(--paper); }
  .brand-lockup {
    position: absolute; left: 50px; top: 172px; display: flex; align-items: center; gap: 14px;
  }
  .brand-lockup .brand-dot { width: 52px; height: 52px; }
  .brand-name--light { color: var(--paper); font-size: 28px; }
  .services {
    position: absolute; left: 440px; top: 75px; list-style: none;
    font-size: 20px; letter-spacing: 1.2px; line-height: 31px; font-weight: 500; white-space: nowrap;
  }
  .services li { display: flex; align-items: center; gap: 16px; }
  .services li::before {
    content: ""; width: 12px; height: 12px; border-radius: 50%; background: var(--accent); flex: none;
  }

  /* Front side */
  .card--front { background: var(--paper); color: var(--text-dark); }
  .name-band { position: absolute; left: 0; top: 30px; }
  .person { position: absolute; left: 40px; top: 48px; }
  .person-name { color: var(--accent); font-weight: 700; font-size: 34px; letter-spacing: 4px; text-transform: uppercase; }
  .person-title { color: var(--paper); font-size: 18px; letter-spacing: 1px; margin-top: 2px; }
  .contact { position: absolute; left: 40px; top: 222px; list-style: none; font-size: 19px; letter-spacing: 0.8px; line-height: 34px; }
  .contact li { display: flex; align-items: center; gap: 12px; }
  .contact svg { width: 16px; height: 16px; flex: none; }
  .contact .web-accent { color: var(--accent); }
  .front-lockup { position: absolute; right: 40px; bottom: 30px; display: flex; align-items: center; gap: 14px; }
  .front-lockup .brand-dot { width: 44px; height: 44px; }
  .brand-name--dark { color: var(--text-dark); font-size: 30px; }
</style>
</head>
<body>
  <section class="card card--back" aria-label="Card back">
    <div class="brand-lockup">
      <span class="brand-dot"></span>
      <span class="brand-name brand-name--light">Lume Vantor</span>
    </div>
    <ul class="services">
      <li>Eyewear Sales</li>
      <li>Admin Duties</li>
      <li>Revenue Collection</li>
      <li>Leadership</li>
      <li>Tech Adoption</li>
      <li>COGS Reduction</li>
      <li>Product Sourcing</li>
      <li>Medical Growth</li>
    </ul>
  </section>

  <section class="card card--front" aria-label="Card front">
    <svg class="name-band" width="720" height="150" viewBox="0 0 720 150" aria-hidden="true">
      <polygon points="0,0 620,0 720,70 720,150 560,150 0,100" fill="var(--ink)"/>
    </svg>
    <div class="person">
      <p class="person-name">Dalton Vesk</p>
      <p class="person-title">CEO</p>
    </div>
    <ul class="contact">
      <li>
        <svg viewBox="0 0 16 16" aria-hidden="true"><path d="M4 1 L6.5 4 L5 6 Q7 10 10 11 L12 9.5 L15 12 L13 15 Q5 14 1 3 Z" fill="var(--accent)"/></svg>
        847-302-6194
      </li>
      <li>
        <svg viewBox="0 0 16 16" aria-hidden="true"><rect x="1.5" y="3.5" width="13" height="9" fill="none" stroke="var(--accent)" stroke-width="1.5"/><path d="M1.5 3.5 L8 9 L14.5 3.5" fill="none" stroke="var(--accent)" stroke-width="1.5"/></svg>
        dalton@lumevantor.net
      </li>
      <li>
        <svg viewBox="0 0 16 16" aria-hidden="true"><circle cx="8" cy="8" r="6.5" fill="none" stroke="var(--accent)" stroke-width="1.4"/><ellipse cx="8" cy="8" rx="3" ry="6.5" fill="none" stroke="var(--accent)" stroke-width="1.2"/><path d="M1.5 8 H14.5" stroke="var(--accent)" stroke-width="1.2"/></svg>
        <span>www.<span class="web-accent">lumevantor</span>.net</span>
      </li>
    </ul>
    <div class="front-lockup">
      <span class="brand-dot"></span>
      <span class="brand-name brand-name--dark">Lume Vantor</span>
    </div>
  </section>
</body>
</html>
```